website design + images

We need a very appealing website design, layout and images for a sales analytics and sales productivity services company based in San Ramon, California. We need a good design for the home page and a template for all other pages (total 2 designs), and images for all inner pages (center column/banner images, and right hand top corner small images). There are about 18 inner pages.
Updates

Our existing website is www.corvexa.com
Our corporate colours are the ones that are there on the website. The logo is also shown. We will be changing the tagline to "accelerating revenue" or equivalent of that.

Please use the document "website for corvexa - template v2.doc" that I just uploaded for any reference to the content, navigation and wireframes. A few more clarifications are provided mainly for the link "Solutions".

Hemant Loravi

Hi,
We just uploaded ver 4 of the website template. There is more elaboration provided around the sublinks / sections for Solutions. Pls review and do get back if you need any clarifications.

Rgds
Hemant Loravi

Hi all,
We have so far received a few good designs. The designs are more or less on the right track. I would like to urge all of you to use the content and navigation provided in the document attached to our brief "website for corvexa - template v4.doc".  Please DO NOT use the content in our existing website www.corvexa.com . That is very old. We mentioned it only for reference to colour theme and broad details.

We have totally 13 sections in Solutions pages. They may be designed as a tree of links - first level sublinks - second level sublinks or links - first level sublinks and the remaining as sections within the first level sublinks pages. The page design would remain the same for all inner pages except careers. But after finalizing the design for the inner page, we will need images for the different inner pages.

Rgds
Hemant Loravi

Hi,
Thank you all for participation and very good designs. We are quite happy with what we have seen. We have now shortlisted about 4 vendors and sending invididual feedback to them for further improvement. We will be finalizing by Monday or Tuesday.  To the vendors who do not get feedback from us, thank you very much for participation. We may still do business in future for some of our other needs. 
The following are the process steps / expectations going forward, 
1. Feedback to the shortlisted designers and inviting improvements.
2. Review of the improved designs and further shortlist & feedback or direct finalization.
3. The design should be in 1024*768
2. Number of page designs = 2 (home page, inner page).
4. Home page design: instead of delivery model and customers, show one link "Why Us".
4. Solutions page design:  We will be needing an image in center column of solutions page that in a nutshell gives all the different types of solutions we provide. The entire set of solutions is in our attached document website for corvexa - template v4 and I am just uploading v5 with more description on sublinks.
5. After selection, we will be needing images for all the solution pages (total 12 pages under solutions + one solutions page), 1 image for Why Us?, 1 for Careers, and 3 for company (about us/ team, core values, ...) = total 18

Rgds
Hemant Loravi

Target Market(s)

We are a sales analytics and sales productivity services company. We help B2B companies with: sales planning; sales operations and sales measurement. The characteristics of our customers are:
- B2B medium enterprises (USD 100M- USD 2B in revenue) in the US
- Primary target verticals are: high-tech, engineering and professional services firms
- Our primary target customers titles are VP of Sales or VP of marketing; we could be selling to the CEO at companies with revenues below $200M

Industry/Entity Type

Consulting

Requirements
Must have
• - Clean, uncluttered design
• - Easy navigation; minimum clicks
Nice to have
• We have already built a content management system and wireframes for this site. To the extent possible, it would be great to leverage the wireframe structure we built, provided you don’t have to compromise on the look and feel and navigation of the site. Below is what we currently have as banner sizes and resolutions are:
• Home page banner size: 950 * 250’
• All pages – center top - image size: 558 * 160
• All pages – right hand top image – 175*135’

```html
<!DOCTYPE html>
<html lang="en">
<head>
<meta charset="utf-8">
<title>Corvexa – Careers</title>
<link href="https://fonts.googleapis.com/css2?family=Noto+Sans:wght@400;700&family=Fira+Sans:wght@500;600&display=swap" rel="stylesheet">
<style>
:root{
  --page-bg:#f3f3f3;
  --stripe:#ececec;
  --blue-dark:#2f7fc8;
  --blue-mid:#5d9fdc;
  --blue-light:#bcd8f2;
  --teal:#17a8b8;
  --orange:#d9620f;
  --text:#4a4a4a;
  --text-soft:#666;
  --nav-text:#1b3d6e;
  --link:#1b3d6e;
  --line:#cfd4da;
  --input-line:#a9c6e4;
  --green:#5a9a1a;
}
*{box-sizing:border-box;margin:0;padding:0}
html,body{width:1200px;height:739px;overflow:hidden}
body{
  position:relative;
  font-family:"Noto Sans",sans-serif;
  color:var(--text);
  background:repeating-linear-gradient(135deg,var(--page-bg) 0 3px,var(--stripe) 3px 4px);
}
.header{position:absolute;left:0;top:0;width:1200px;height:77px;background:linear-gradient(#fff 0 55%,#eceff2)}
.brand{position:absolute;left:223px;top:24px;display:flex;align-items:center;gap:8px;font-size:26px;color:var(--blue-dark);letter-spacing:1px}
.brand-dot{width:16px;height:16px;border-radius:50%;background:var(--blue-dark)}
.utility{position:absolute;left:822px;top:5px;display:flex;align-items:center;gap:4px;font-size:10.5px;color:var(--link)}
.utility svg{margin-right:2px}
.main-nav{position:absolute;left:448px;top:49px;display:flex;gap:2.5px}
.main-nav a{width:89px;height:26px;display:flex;align-items:center;justify-content:center;font-size:12.5px;color:var(--nav-text);text-decoration:none;border:1px solid #d3d6da;border-bottom:none;background:linear-gradient(#fdfdfd,#e7eaee)}
.main-nav a.active{color:#2b6cb3}
.band{position:absolute;left:0;top:77px;width:1200px;height:115px;background:linear-gradient(90deg,var(--blue-dark),var(--blue-light) 25%,#fff 50%,var(--blue-light) 75%,var(--blue-dark))}
.banner{position:absolute;left:204px;top:77px;width:792px;height:115px;background:linear-gradient(90deg,#9ec4ea,#e8f1fa 40%,#bcd6f0 90%);border-radius:0 0 6px 6px}
.banner-photo{position:absolute;left:0;top:0;width:129px;height:115px;background:linear-gradient(135deg,#d9c2a8,#a8b8c8 60%,#9fc0e4);border-radius:0 0 0 6px}
.banner-card{position:absolute;left:183px;top:18px;width:484px;height:80px;background:#fff;border-radius:8px;box-shadow:0 1px 3px rgba(0,0,0,.2);padding:13px 36px}
.banner-card h1{font-family:"Fira Sans",sans-serif;font-weight:500;font-size:19px;color:var(--teal);line-height:1}
.banner-card p{margin:10px 0 0 7px;font-size:10.5px;line-height:15px;color:var(--text-soft)}
.content{position:absolute;left:198px;top:205px;width:791px;height:433px;background:#fff;border:1px solid var(--line);border-radius:4px}
.ornament{position:absolute;border-radius:40%;background:radial-gradient(#dfeaf6,rgba(223,234,246,0))}
.sidebar{position:absolute;left:16px;top:11px;width:172px;height:409px;border:1px solid #dde0e4;border-radius:3px;background:#fafafa;overflow:hidden}
.sidebar h2{position:absolute;left:9px;top:8px;font-family:"Fira Sans",sans-serif;font-weight:600;font-size:15px;color:var(--teal)}
.sidebar a{position:absolute;font-size:11px;color:#333;text-decoration:none;white-space:nowrap}
.sidebar a.top::before{content:"";position:absolute;left:-12px;top:4px;width:5px;height:7px;border-left:1px dotted #777;border-top:1px dotted #777}
.sidebar a.sub{font-size:10.5px}
.sidebar a.sub::before{content:"··›";position:absolute;left:-20px;top:-1px;color:var(--green);font-weight:700;letter-spacing:1px}
.main{position:absolute;left:208px;top:20px;width:566px}
.main h2{font-family:"Fira Sans",sans-serif;font-weight:600;font-size:14.5px;color:var(--teal);line-height:20px}
.main p{font-size:10.8px;line-height:16.7px;text-align:justify;margin-top:4px}
.main p + p{margin-top:4px}
.main h3{font-size:10.8px;font-weight:700;color:var(--orange);margin-top:7px;letter-spacing:.3px;line-height:15px}
.resume-form{position:relative;height:240px}
.resume-form label{position:absolute;left:0;width:121px;text-align:right;font-size:10.3px;line-height:15px;color:#666}
.resume-form .field{position:absolute;left:129px;width:195px;height:15px;border:1px solid var(--input-line);background:#fff}
.resume-form .field.area{height:40px}
.submit{position:absolute;left:261px;top:212px;width:61px;height:18px;border-radius:6px;background:linear-gradient(#5bb8ea,#1577b8);border:1px solid #1468a3;color:#fff;font-size:10.5px;display:flex;align-items:center;justify-content:center}
.footer{position:absolute;left:6px;top:649px;width:1194px;height:67px;background:linear-gradient(#a6cbf2,#6aa4e6);border-radius:4px 0 0 4px;display:flex;align-items:center;justify-content:center;font-size:10.8px;color:#1b2f55}
</style>
</head>
<body>
<header class="header">
  <div class="brand"><span class="brand-dot"></span>corvexa</div>
  <nav class="utility">
    <svg width="20" height="20" viewBox="0 0 20 20" aria-hidden="true"><circle cx="8" cy="8" r="5.5" fill="#dfeefb" stroke="#6a8fb8" stroke-width="1.6"/><line x1="12" y1="12" x2="18" y2="18" stroke="#3d5573" stroke-width="2.6" stroke-linecap="round"/></svg>
    <span>Sign in</span> | <span>Contact us</span> | <span>Sitemap</span>
  </nav>
  <nav class="main-nav">
    <a class="active" href="#">Home</a><a href="#">Solutions</a><a href="#">Why Us</a><a href="#">Buy Now</a><a href="#">Company</a><a href="#">Careers</a>
  </nav>
</header>
<div class="band"></div>
<section class="banner">
  <div class="banner-photo" role="img" aria-label="Photo of a smiling professional woman in an office"></div>
  <div class="banner-card">
    <h1>Careers</h1>
    <p>Lorem Ipsum is simply dummy text of the printing and typesetting industry.<br>Lorem Ipsum has been the industry's standard</p>
  </div>
</section>
<main class="content">
  <div class="ornament" role="img" aria-label="Faint floral ornament" style="left:655px;top:135px;width:130px;height:260px"></div>
  <aside class="sidebar">
    <div class="ornament" role="img" aria-label="Faint floral ornament" style="left:70px;top:170px;width:110px;height:240px"></div>
    <h2>Welcome</h2>
    <a class="top" href="#" style="left:28px;top:39px">Home</a>
    <a class="top" href="#" style="left:28px;top:61px">Solutions</a>
    <a class="sub" href="#" style="left:41px;top:80px">Managed Services</a>
    <a class="sub" href="#" style="left:41px;top:105px">Consulting</a>
    <a class="sub" href="#" style="left:41px;top:130px">Contract Staffing</a>
    <a class="top" href="#" style="left:29px;top:151px">Why Us</a>
    <a class="top" href="#" style="left:30px;top:171px">Buy Now</a>
    <a class="top" href="#" style="left:29px;top:193px">Company</a>
    <a class="sub" href="#" style="left:39px;top:215px">About Us</a>
    <a class="sub" href="#" style="left:39px;top:240px">Our Culture &amp; Values</a>
    <a class="sub" href="#" style="left:39px;top:265px">Philanthropy</a>
    <a class="sub" href="#" style="left:39px;top:290px">Careers</a>
    <a class="sub" href="#" style="left:39px;top:315px">Contact Us</a>
    <a class="top" href="#" style="left:31px;top:334px">Careers</a>
  </aside>
  <article class="main">
    <h2>Careers</h2>
    <p>We are an employee-focused company consisting of passionate individuals who work hard and play hard. Do you want to be the best at what you do? Do you thrive in challenging, fast-paced environments? Do you consider continuous learning and a passion for excellence two of your driving forces? If so, let's talk. Our doors are always open to exceptional individuals.</p>
    <p>Join our team. Learn, contribute, and make a difference. Be appreciated and rewarded.</p>
    <h3>Submit your resume</h3>
    <form class="resume-form">
      <label style="top:13px">First Name:</label><span class="field" style="top:13px"></span>
      <label style="top:37px">Last Name:</label><span class="field" style="top:37px"></span>
      <label style="top:63px">E-Mail:</label><span class="field" style="top:64px"></span>
      <label style="top:88px">Confirm E-Mail:</label><span class="field" style="top:89px"></span>
      <label style="top:113px">Country:</label><span class="field" style="top:114px"></span>
      <label style="top:138px">Attach Resume:</label><span class="field" style="top:140px"></span>
      <label style="top:163px">Comments:</label><span class="field area" style="top:164px"></span>
      <span class="submit">Submit</span>
    </form>
  </article>
</main>
<footer class="footer">© 2010 Corvexa, Inc. | Contact Us | Sign in (register) | Contact us | Sitemap</footer>
</body>
</html>
```